Packaging for a LED beauty Mirror Box

We need packaging designed for a LED beauty mirror that we are selling.
An example of the box shape, size and design is attached (this is not our design and is only so that you can understand the type of box we will be working with). The dimensions are 28 X 17.5 X 7.5cm. You can send each side of the box (eg, top, front, side) as separate images.

The product we are selling can be found here, so you can have a look so you better understand the product: https://www.pemrashop.com.au/products/brightset-beauty-makeup-mirror

MAIN IDEAS:

# Black box all over
# White Logo on the top of the box. Our logo uses the font vonique_92 from typevault but it also included as an attachment.

#Include the product name in a cool font (see our home page banner for a ROUGH idea. The banner is pretty poor quality as it was created by myself but it can give you a basic idea). A photo of the actual product is not necessary as I think it would be very hard to incorporate due to the colour. But if you are able to and think you can make it work would be happy to see what you can come up with.

# On the front side of the box we would like something like " like, follow, and tag us to be featured"
and then below have the instagram logo and facebook logo with our tags which is:
Instagram = @pemrashop
facebook = www.kindalink.com/pemrashop

Reason: Set deadline for 1 day but nobody responded so I am extending it for 5 more days. Get your designs in early as we need to go into production this week.

Target Market(s)

18 - 45 years old

Requirements
Must have
• - White logo on top of box
• - Product name 'The BrightSet Portable Mirror' - emphasise the "BrightSet" and portable mirror can be smaller. Up to the designer how you see fit. Also on top of box.
• - the front of the box must have our instagram and facebook details
• - must look expensive and high quality
Nice to have
• Would be nice to have the 'brightset' product name emphasised in a cool font. Weather it is gold or has some sort of glow effect to it.

```html
<!DOCTYPE html>
<html lang="en">
<head>
<meta charset="utf-8">
<title>pemra shop – BrightSet Portable Mirror – Box Top</title>
<link rel="stylesheet" href="https://fonts.googleapis.com/css2?family=Montserrat:wght@300;400&family=Mr+Dafoe&display=swap">
<style>
  :root {
    --page: #ffffff;
    --box-black: #231f20;
    --logo-white: #ffffff;
    --gold: #cfa34b;
    --gold-pale: #dab872;
    --bronze: #b07a2a;
    --label-ink: #231f20;
  }
  * { margin: 0; padding: 0; box-sizing: border-box; }
  html, body {
    width: 1200px;
    height: 1000px;
    overflow: hidden;
    background: var(--page);
  }
  .canvas {
    position: relative;
    width: 1200px;
    height: 1000px;
  }
  .box-top {
    position: absolute;
    left: 173px;
    top: 212px;
    width: 870px;
    height: 556px;
    background: var(--box-black);
    overflow: hidden;
  }
  .box-top__artwork {
    position: absolute;
    inset: 0;
    width: 100%;
    height: 100%;
  }
  .brand-logo {
    position: absolute;
    left: 38px;
    top: 30px;
    font-family: "Montserrat", sans-serif;
    font-weight: 300;
    font-size: 50px;
    letter-spacing: -1.5px;
    color: var(--logo-white);
    line-height: 1;
  }
  .product-name {
    font-family: "Mr Dafoe", cursive;
    font-weight: 400;
    color: var(--gold);
    line-height: 1;
  }
  .product-name__hero,
  .product-name__sub {
    position: absolute;
    white-space: nowrap;
  }
  .product-name__hero {
    right: 34px;
    top: 282px;
    font-size: 82px;
  }
  .product-name__sub {
    right: 38px;
    top: 388px;
    font-size: 56px;
  }
  .side-label {
    position: absolute;
    left: 0;
    width: 1200px;
    top: 806px;
    text-align: center;
    font-family: "Montserrat", sans-serif;
    font-weight: 400;
    font-size: 80px;
    color: var(--label-ink);
    line-height: 1;
  }
</style>
</head>
<body>
<main class="canvas">
  <section class="box-top">
    <svg class="box-top__artwork" viewBox="0 0 870 556" role="img"
         aria-label="Flowing gold and bronze wave artwork across the lower part of the lid">
      <defs>
        <linearGradient id="gold-sweep" x1="0" y1="0" x2="1" y2="0.4">
          <stop offset="0" stop-color="var(--bronze)"/>
          <stop offset="0.3" stop-color="var(--gold-pale)"/>
          <stop offset="1" stop-color="var(--gold)"/>
        </linearGradient>
      </defs>
      <path fill="url(#gold-sweep)"
            d="M0,235 C180,255 420,430 620,505 C740,548 820,535 870,520 V556 H0 Z"/>
    </svg>

    <div class="brand-logo">pemra shop</div>

    <h1 class="product-name">
      <span class="product-name__hero">BrightSet</span>
      <span class="product-name__sub">Portable Mirror</span>
    </h1>
  </section>

  <p class="side-label">Top</p>
</main>
</body>
</html>
```